Modern Website For Law Firm Lawyer Melbourne, Australia Coded

We are looking for a modern and sophisticated website design. We would prefer the site to be based on WordPress given it is intuitive and some of our staff have experience using it.

Our law firm is based in Melbourne, Australia and we deal with property. The website must be hosted on a reliable Australian server.

We would also appreciate it if the designer can provide some guidance about how to make changes/upload content, such as photos and articles. We are happy to pay for this advice.

We prefer classic fonts in black or grey. We would also like a dash of colour so please use a green, blue or aqua colour palette that is consistent with our logo attached.

We do not want any law related images - scales of justice, gavel or the like.

Our ultimate goal is to communicate that the firm is professional, affordable, modern, dynamic, knowledgeable and one with the community.

We would like the following pages/sections/icons:

1. Who We Are - we will provide content.

2. Our Services - 1. Property 2. Wills, 3. Powers of Attorney 4. Probate & Estate Administration 5.Consultancy & Agency- we will provide content for each of these sections.

3. Articles - we already have approximately 20 articles on a wordpress blog and would like to port these articles to the website. We can do this ourselves if the designer can give us instructions about how to do this. We would also like to give clients the option to subscribe to our articles.

4. Contact Us - this should include our firms contact details; location map and we would like to give clients the option to "Request A Quote" directly from the page - i.e they will need to provide their full name, phone number email address, choose subject from drop down menu and type a message that gets sent to our outlook email.

5. Terms and Conditions - we will provide content

We really like the style and photographs used in the following website and want something as close to this as possible:

https://www.brelwick.com/

For privacy reasons, we would prefer to provide content together with all business details once we have decided on the winner.

We will monitor entries closely and promise to provide feedback and guidance on each entry.

This project is guaranteed. If our budget is too low please email us so we can discuss further and perhaps increase our budget. We are reasonable in this regard.

Thank you very much for considering this project.

Target Market(s)

General public, professionals, lawyers and conveyancers

Industry/Entity Type

Law Firm

Coding

Coded - Design and coding required

Number of Pages Required

1 page

Font styles to use
Sans Serif

Colors
33b8a4
33a6d7
0692cd
3176b5
00a990
9bcb3c
86cfc6
cadf82
85acd3

Requirements
Must have
• 1. Site must be coded and hosted on a reliable Australian server and it would be much appreciated if the deisgner provides instructions about how to add photos, blog articles etc-
• 2. The site must be secure and have green lock at top of page
• 3. Request A Quote - name, email, phone, drop down subject, message - email to our outlook email
• 4. Article Subscription
• 5. Domain (we have already purchased)
• 6. Location map
• 7. Facebook, LinkedIn, Instagram Icons
• 8. Membership icons in this order - VLQ Member > Coastal Women Advocates > Guide For Counsel > Creature Foundation > Tovra > Parcelnet > Vek QA logos attached to go on bottom of page
• 9. Testimonials
Nice to have
• A modern, sophisticated website like:
• https://www.brelwick.com/ - we really like the style of the brelwick photographs
• We also really like this design by Rk of Sketch swarm:
• https://www.sketchswarm.com.au/design/58201946
Should not have
• Law related images - scales of justice gavel and the like

```html
<!DOCTYPE html>
<html lang="en">
<head>
<meta charset="utf-8">
<title>Ridgeway Lawyers – Melbourne</title>
<link rel="stylesheet" href="https://fonts.googleapis.com/css2?family=Courgette&family=Open+Sans:wght@400;600;700&display=swap">
<style>
:root{
  --blue:#0692cd;
  --blue-dark:#0a7fb8;
  --teal:#33b8a4;
  --ink:#222;
  --grey:#555;
  --pale:#eef5fb;
  --white:#fff;
  --script:"Courgette",cursive;
  --sans:"Open Sans",Arial,sans-serif;
}
*{box-sizing:border-box;margin:0;padding:0}
html,body{width:1200px;height:3180px;overflow:hidden;background:var(--white);font-family:var(--sans);color:var(--ink)}
.page{position:relative;width:1200px;height:3180px}
.abs{position:absolute}

/* header */
.brand{left:100px;top:24px;display:flex;align-items:center;gap:14px}
.brand-mark{width:64px;height:64px;border-radius:50%;background:var(--blue)}
.brand-name{font-size:22px;font-weight:600;color:var(--grey);line-height:1.05;letter-spacing:.5px}
.brand-name small{display:block;font-size:15px;font-weight:600}
.contact-top{top:22px;right:100px;display:flex;gap:36px;font-size:16px;color:var(--blue)}
.contact-top span{display:flex;align-items:center;gap:12px}
.contact-top .ic{width:32px;height:32px;border-radius:50%;background:var(--blue);display:flex;align-items:center;justify-content:center}
.contact-top .ic.teal{background:var(--teal)}
.contact-top .phone{color:var(--teal)}
.nav{top:80px;right:100px;display:flex;gap:26px;font-size:15px;font-weight:600;color:var(--ink)}
.nav .active{color:var(--blue)}

/* hero */
.hero{left:0;top:125px;width:1200px;height:512px;background:linear-gradient(180deg,#4f6b86 0%,#7d8d9c 45%,#4c4a44 75%,#2c2a26 100%)}
.hero h1{position:absolute;top:120px;width:100%;text-align:center;font-family:var(--script);font-weight:400;font-size:68px;color:var(--white)}
.hero p{position:absolute;top:232px;left:250px;width:700px;text-align:center;font-size:15px;font-weight:600;line-height:1.7;color:var(--white)}
.hero .arrow{position:absolute;top:232px}

/* intro boxes */
.intro{left:100px;top:550px;width:1000px;height:296px;display:flex;box-shadow:0 18px 22px -10px rgba(0,0,0,.3)}
.intro-box{flex:1;padding:34px 28px;color:var(--white)}
.intro-box.blue{background:var(--blue)}
.intro-box.teal{background:var(--teal)}
.intro-box h3{font-family:var(--script);font-weight:400;font-size:24px;margin:26px 0 14px}
.intro-box p{font-size:13.5px;font-weight:600;line-height:1.75}

/* section heading */
.sec-title{width:1200px;left:0;text-align:center;font-family:var(--script);font-weight:400;font-size:31px;color:var(--blue)}
.rule{width:110px;height:2px;background:var(--blue);left:545px}

/* service cards */
.card{top:1068px;width:308px;height:397px;border:2px solid var(--blue);border-radius:4px;text-align:center}
.card.teal{border-color:var(--teal)}
.card .icon{width:130px;height:130px;border-radius:50%;background:var(--blue);margin:30px auto 0;display:flex;align-items:center;justify-content:center}
.card.teal .icon{background:var(--teal)}
.card h4{font-size:22px;font-weight:600;color:var(--blue);margin:24px 0 12px}
.card.teal h4{color:var(--teal)}
.card p{font-size:14px;line-height:1.6;color:var(--grey);padding:0 22px}
.btn{display:inline-block;margin-top:26px;padding:14px 20px;background:var(--blue);color:var(--white);font-size:13px;font-weight:600;border-radius:2px}
.card.teal .btn{background:var(--teal)}

/* testimonial */
.photo-meeting{left:100px;top:1550px;width:726px;height:402px;background:linear-gradient(120deg,#5d6a78 0%,#9aa6b2 40%,#c9ccd0 60%,#6f7882 100%)}
.quote{left:650px;top:1747px;width:450px;height:296px;background:var(--blue);color:var(--white);padding:26px 28px}
.quote .mark{font-family:Georgia,serif;font-size:60px;line-height:.6;font-weight:700}
.quote p{font-size:17.5px;font-weight:600;line-height:1.75;margin-top:14px}
.quote .who{font-size:16px;font-weight:600;margin-top:14px}
.quote .close{position:absolute;right:26px;top:168px}
.dots{display:flex;gap:4px;margin-top:18px}
.dots i{width:12px;height:12px;border:1.5px solid var(--white);border-radius:50%}
.dots i:first-child{background:var(--white)}

/* blog */
.blog{left:0;top:2142px;width:1200px;height:438px;background:var(--pale)}
.post{top:2342px;display:flex;gap:16px;width:480px}
.post .thumb{width:197px;height:155px;flex:none}
.post h5{font-size:18px;font-weight:400;color:var(--ink);margin-top:2px}
.post .date{font-size:12px;font-style:italic;color:var(--teal);margin:6px 0 8px}
.post p{font-size:13px;line-height:1.7;color:var(--grey)}

/* contact */
.map{left:98px;top:2657px;width:482px;height:393px;background:linear-gradient(135deg,#d9d6c8 0%,#c9cfc2 40%,#a9c7d8 70%,#d6d3c6 100%);border:2px solid #ccc}
.contact-title{left:663px;top:2700px;font-family:var(--script);font-weight:400;font-size:31px;color:var(--blue)}
.contact-rule{left:663px;top:2756px;width:92px;height:2px;background:var(--blue)}
.info{left:663px;display:flex;align-items:center;gap:20px;font-size:15px;color:var(--ink);line-height:1.55}
.info .ring{width:50px;height:50px;border:2px solid var(--blue);border-radius:50%;display:flex;align-items:center;justify-content:center;flex:none}
.info b{font-weight:700}
.foot-rule{left:100px;top:3100px;width:1000px;height:2px;background:var(--blue)}
.copy{left:0;top:3132px;width:1200px;text-align:center;font-size:13px;font-weight:600;color:var(--ink)}
</style>
</head>
<body>
<div class="page">

  <header>
    <div class="abs brand"><span class="brand-mark"></span><div class="brand-name">RIDGEWAY<small>LAWYERS</small></div></div>
    <div class="abs contact-top">
      <span><i class="ic"><svg width="16" height="12" viewBox="0 0 16 12" fill="none" stroke="#fff" stroke-width="1.6"><rect x="1" y="1" width="14" height="10"/><path d="M1 1l7 6 7-6"/></svg></i>info@ridgewaylawyers.com</span>
      <span class="phone"><i class="ic teal"><svg width="14" height="14" viewBox="0 0 24 24" fill="#fff"><path d="M6.6 10.8a15 15 0 006.6 6.6l2.2-2.2a1 1 0 011-.25 11.4 11.4 0 003.6.6 1 1 0 011 1V20a1 1 0 01-1 1A17 17 0 013 4a1 1 0 011-1h3.5a1 1 0 011 1 11.4 11.4 0 00.6 3.6 1 1 0 01-.25 1z"/></svg></i>+180 041 7729</span>
    </div>
    <nav class="abs nav"><span class="active">Home</span><span>Who we Are</span><span>Our Services</span><span>Articles</span><span>Terms &amp; Conditions</span><span>Contact Us</span></nav>
  </header>

  <section class="abs hero" role="img" aria-label="Photo of the Melbourne city skyline and river bridge under a cloudy sky">
    <h1>Ridgeway Lawyers in Melbourne</h1>
    <p>Nemo enim ipsam voluptatem quia voluptas sit aspernatur aut odit aut fugit, sed quia conse quuntur magni dolores eos qui ratione voluptatem sequi nesciunt.</p>
    <svg class="arrow" style="left:36px" width="22" height="50" viewBox="0 0 22 50" fill="none" stroke="#fff" stroke-width="2.5"><path d="M20 2L3 25l17 23"/></svg>
    <svg class="arrow" style="right:36px" width="22" height="50" viewBox="0 0 22 50" fill="none" stroke="#fff" stroke-width="2.5"><path d="M2 2l17 23L2 48"/></svg>
  </section>

  <section class="abs intro">
    <div class="intro-box blue">
      <svg width="58" height="58" viewBox="0 0 58 58" fill="none" stroke="#fff" stroke-width="4"><rect x="4" y="4" width="34" height="50" rx="8"/><path d="M12 20h18M12 30h18M12 40h12M48 18v36"/><circle cx="48" cy="9" r="3" fill="#fff"/></svg>
      <h3>Who We Are</h3>
      <p>Nemo enim ipsam voluptatem quia voluptas sit aspernatur aut odit aut fugit, sed quia consequuntur magni dolores eos qui ratione vo luptatem sequi nesciunt.</p>
    </div>
    <div class="intro-box teal">
      <svg width="58" height="58" viewBox="0 0 58 58" fill="none" stroke="#fff" stroke-width="3.5"><path d="M12 6h36v40a6 6 0 01-6 6H8a6 6 0 006-6V10a4 4 0 00-4-4h2z"/><path d="M20 16h20M20 24h20M20 32h20M20 40h12"/></svg>
      <h3>What We Do</h3>
      <p>Nemo enim ipsam voluptatem quia voluptas sit aspernatur aut odit aut fugit, sed quia consequuntur magni dolores eos qui ratione vo luptatem sequi nesciunt.</p>
    </div>
  </section>

  <h2 class="abs sec-title" style="top:936px">Ridgeway Lawyers Services</h2>
  <div class="abs rule" style="top:1003px"></div>

  <article class="abs card" style="left:100px">
    <div class="icon"><svg width="64" height="56" viewBox="0 0 64 56" fill="#fff"><circle cx="20" cy="20" r="10"/><path d="M2 52c0-12 8-20 18-20s18 8 18 20z"/><rect x="36" y="6" width="7" height="30"/><rect x="45" y="4" width="7" height="32"/><rect x="54" y="8" width="7" height="28"/></svg></div>
    <h4>Our Expertise</h4>
    <p>Sed ut perspiciatis unde omnis iste natus error sit voluptatem accusantium dolorem que laudantium.</p>
    <span class="btn">Read More</span>
  </article>
  <article class="abs card teal" style="left:446px">
    <div class="icon"><svg width="48" height="62" viewBox="0 0 48 62" fill="none" stroke="#fff" stroke-width="4"><path d="M24 54S8 36 8 22a16 16 0 0132 0c0 14-16 32-16 32z"/><circle cx="24" cy="22" r="6"/><path d="M6 58h36"/></svg></div>
    <h4>Our Locations</h4>
    <p>Sed ut perspiciatis unde omnis iste natus error sit voluptatem accusantium dolorem que laudantium.</p>
    <span class="btn">Read More</span>
  </article>
  <article class="abs card" style="left:792px">
    <div class="icon"><svg width="60" height="50" viewBox="0 0 60 50" fill="#fff"><path d="M22 4h16a3 3 0 013 3v5h-4V8H23v4h-4V7a3 3 0 013-3z"/><rect x="2" y="12" width="56" height="36" rx="5"/><rect x="2" y="26" width="56" height="3" fill="#0692cd"/><rect x="26" y="23" width="8" height="9" rx="1" fill="#0692cd"/></svg></div>
    <h4>Careers</h4>
    <p>Sed ut perspiciatis unde omnis iste natus error sit voluptatem accusantium dolorem que laudantium.</p>
    <span class="btn">Read More</span>
  </article>

  <div class="abs photo-meeting" role="img" aria-label="Photo of business people shaking hands across a meeting table"></div>
  <blockquote class="abs quote">
    <div class="mark">&ldquo;</div>
    <p>Enim ad minima veniam, quis nostrum exer citationem ullam corporis suscipit labori osam, nisi ut aliquid ex ea commodi conse quatur autem vel eum iures...</p>
    <div class="who">- Mark Ellison</div>
    <div class="mark close">&rdquo;</div>
    <div class="dots"><i></i><i></i><i></i><i></i><i></i></div>
  </blockquote>

  <section class="abs blog"></section>
  <h2 class="abs sec-title" style="top:2214px">Latest Blog Posts</h2>
  <div class="abs rule" style="top:2280px;left:563px;width:74px"></div>

  <article class="abs post" style="left:100px">
    <div class="thumb" role="img" aria-label="Photo of hands signing a document" style="background:linear-gradient(135deg,#6f5a4a,#c9c3bb 60%,#8a8580)"></div>
    <div><h5>Nemo enim ipsam</h5><div class="date">March 20, 2016</div><p>Nemo enim ipsam voluptatem quia volup tas sit aspernatur aut odit aut fugit, sed quia consequuntur magni dolores eos qui ratione.</p></div>
  </article>
  <article class="abs post" style="left:615px">
    <div class="thumb" role="img" aria-label="Photo of two professionals shaking hands in an office" style="background:linear-gradient(135deg,#2b2b2f,#7d7a78 55%,#3a3838)"></div>
    <div><h5>Voluptatem quia voluptas</h5><div class="date">March 20, 2016</div><p>Nemo enim ipsam voluptatem quia volup tas sit aspernatur aut odit aut fugit, sed quia consequuntur magni dolores eos qui ratione.</p></div>
  </article>

  <div class="abs map" role="img" aria-label="Street map of central Melbourne showing the office location"></div>
  <h2 class="abs contact-title">Contact Us</h2>
  <div class="abs contact-rule"></div>
  <div class="abs info" style="top:2806px">
    <span class="ring"><svg width="18" height="24" viewBox="0 0 18 24" fill="none" stroke="#0692cd" stroke-width="2"><path d="M9 22S2 14 2 8.5a7 7 0 0114 0C16 14 9 22 9 22z"/><circle cx="9" cy="8.5" r="2.5"/></svg></span>
    <div><b>Ridgeway Lawyers,</b><br><span style="font-size:13.5px">Unit 318, Kelmore Business Park 4,<br>Melbourne, Australia</span></div>
  </div>
  <div class="abs info" style="top:2892px">
    <span class="ring"><svg width="20" height="20" viewBox="0 0 24 24" fill="#0692cd"><path d="M6.6 10.8a15 15 0 006.6 6.6l2.2-2.2a1 1 0 011-.25 11.4 11.4 0 003.6.6 1 1 0 011 1V20a1 1 0 01-1 1A17 17 0 013 4a1 1 0 011-1h3.5a1 1 0 011 1 11.4 11.4 0 00.6 3.6 1 1 0 01-.25 1z"/></svg></span>
    <div><b>Phone:</b> +180 041 7729</div>
  </div>
  <div class="abs info" style="top:2957px">
    <span class="ring"><svg width="22" height="16" viewBox="0 0 22 16" fill="none" stroke="#0692cd" stroke-width="1.8"><rect x="1" y="1" width="20" height="14"/><path d="M1 1l10 8 10-8"/></svg></span>
    <div><b>Mail:</b> info@ridgewaylawyers.com</div>
  </div>

  <div class="abs foot-rule"></div>
  <footer class="abs copy">Copyrights @ 2017 Ridgeway Lawyers. All Rights Reserved.</footer>
</div>
</body>
</html>
```